Juice up my new website for book profits on Borvelt

I have a website that needs a new look. I made a video of the past and in progress website: http://vidloop.example/tk8wpZ2RMA.... here is the site in progress. http://blend.movewellstudio.example/...this will be a WordPress website......https://pagevault.example/web/20180305134456/http://www.pressedtonic-notes.example/

This website is setup to primary sell on Borvelt.

eBook: https://www.borvelt.example/Tonic-Shake-Blends-For-Vital-Days-ebook/dp/K72RRTQMWX/ref=sr_1_4?dchild=1&keywords=Tonic+and+Shake+blends+for+vital+days&qid=1634055930&s=books&sr=1-4

Target Market(s)

Health and weight conscience people

Industry/Entity Type

Health

Number of Pages Required

2 page

Font styles to use
Serif

Requirements
Must have
• slider, sign up form, buy the ebook or hardcopy book.
Nice to have
• happy people drinking juice
Should not have
• Sidebar

```html
<!DOCTYPE html>
<html lang="en">
<head>
<meta charset="utf-8">
<title>Pressed Tonic</title>
<link href="https://fonts.googleapis.com/css2?family=Lora:wght@400;600;700&family=Merriweather:wght@400;700&display=swap" rel="stylesheet">
<style>
:root{
  --blue:#2f9fd8;
  --blue-deep:#2a8fc6;
  --panel:#3aa0d2;
  --grey-bg:#efefef;
  --ink:#555;
  --white:#fff;
  --nav-bg:rgba(20,40,50,.35);
  --accent:#f2a51a;
}
*{margin:0;padding:0;box-sizing:border-box}
html,body{width:1200px;height:2276px;overflow:hidden}
body{font-family:"Lora",Georgia,serif;color:var(--ink);background:var(--white);position:relative}
.hero{position:absolute;left:0;top:0;width:1200px;height:668px;
  background:linear-gradient(120deg,#3b4a2c 0%,#6f8a3a 30%,#c2c9b0 55%,#d86a3a 75%,#5a3a2a 100%)}
.site-nav{position:absolute;left:0;top:0;width:1200px;height:48px;background:var(--nav-bg);display:flex;align-items:center;padding:0 120px 0 178px}
.brand{font-family:"Merriweather",serif;font-weight:700;font-size:16px;color:var(--white);letter-spacing:.5px;white-space:nowrap}
.menu{margin-left:auto;display:flex;gap:24px;font-family:"Lora",serif;font-size:10px;font-weight:600;color:var(--white);text-transform:uppercase}
.search{margin-left:60px;display:flex;align-items:center;gap:8px;color:var(--white);font-size:10px}
.search i{display:block;width:12px;height:12px;border-radius:50%;background:#f2c100}
.hero-copy{position:absolute;left:0;top:362px;width:1200px;text-align:center;color:var(--white);text-shadow:0 2px 6px rgba(0,0,0,.5)}
.hero-copy h1{font-family:"Merriweather",serif;font-weight:700;font-size:38px;line-height:48px}
.hero-copy p{font-size:14px;line-height:20px;margin-top:8px}
.buy{margin-top:18px;display:flex;justify-content:center;gap:14px}
.btn{display:inline-block;height:38px;line-height:38px;padding:0 24px;font-family:"Lora",serif;font-weight:700;font-size:13px;color:var(--white);text-shadow:none;border-radius:3px}
.btn-primary{background:var(--blue)}
.btn-secondary{background:var(--accent)}
.dots{position:absolute;top:626px;left:0;width:1200px;display:flex;justify-content:center;gap:8px}
.dots i{width:10px;height:10px;border-radius:50%;background:rgba(255,255,255,.5)}
.dots i:first-child{background:var(--white)}
.why{position:absolute;left:0;top:668px;width:1200px;height:527px;background:var(--grey-bg);text-align:center}
.sec-title{font-family:"Merriweather",serif;font-weight:700;font-size:23px;color:var(--blue);letter-spacing:1px}
.sec-sub{font-size:11px;color:#888;margin-top:4px}
.why .sec-title{margin-top:52px}
.cards{position:absolute;left:236px;top:117px;display:flex;gap:8px}
.card{position:relative;width:236px;height:345px}
.card .photo{position:absolute;inset:0}
.card span{position:absolute;left:0;bottom:0;width:100%;height:34px;line-height:34px;background:rgba(0,0,0,.45);color:var(--white);font-size:11px}
.arrow{position:absolute;left:934px;top:258px;width:26px;height:54px;background:var(--blue);display:flex;align-items:center;justify-content:center}
.post{position:absolute;left:0;top:1195px;width:1200px;height:365px;display:flex}
.post .photo{width:590px;height:365px;background:linear-gradient(135deg,#e6c9a2,#b98a5e 50%,#7a5a44)}
.post-body{flex:1;background:var(--panel);color:var(--white);padding:58px 96px 0 46px}
.post-body h2{font-family:"Merriweather",serif;font-weight:700;font-size:16px}
.post-body p{font-size:10.5px;line-height:16px;margin-top:12px}
.post-body b{font-weight:700}
.signup{margin-top:18px}
.signup label{display:block;font-size:11px;font-weight:700;margin-bottom:6px}
.signup-row{display:flex}
.signup-field{flex:1;height:34px;background:var(--white);color:#999;font-size:11px;line-height:34px;padding:0 12px;border-radius:3px 0 0 3px}
.signup-btn{height:34px;line-height:34px;padding:0 20px;background:var(--accent);color:var(--white);font-weight:700;font-size:11px;border-radius:0 3px 3px 0}
.videos{position:absolute;left:0;top:1560px;width:1200px;height:440px;text-align:center}
.videos .sec-title{margin-top:78px}
.clips{position:absolute;left:246px;top:135px;display:flex;gap:40px}
.clip{height:240px}
.map{position:absolute;left:0;top:2000px;width:1200px;height:215px;background:linear-gradient(160deg,#e8eadf,#d7dccb 45%,#c9d8b8)}
.footer{position:absolute;left:0;top:2215px;width:1200px;height:61px;background:var(--blue-deep);display:flex;align-items:center;padding:0 170px;color:var(--white)}
.footer .brand{font-size:14px}
.footer small{margin-left:120px;font-size:9px;letter-spacing:.5px}
.social{margin-left:auto;display:flex;gap:14px}
.social i{width:10px;height:10px;border-radius:50%;background:var(--white)}
</style>
</head>
<body>
<header class="hero" role="img" aria-label="Glasses of green juice and orange smoothie with flowers on a cafe table">
  <nav class="site-nav">
    <div class="brand">PRESSED TONIC</div>
    <div class="menu"><span>Home</span><span>Our Book</span><span>Recipes</span><span>The Blog</span><span>Meet Us</span></div>
    <div class="search"><i></i>SEARCH</div>
  </nav>
  <div class="hero-copy">
    <h1>Tonic and Shake Blends For Vital Days</h1>
    <p>Simple fresh blends that restore energy, support weight goals and taste great.<br>Get the ebook or the hardcopy book and start feeling better today.</p>
    <div class="buy">
      <span class="btn btn-primary">Buy the eBook on Borvelt</span>
      <span class="btn btn-secondary">Buy the Hardcopy</span>
    </div>
  </div>
  <div class="dots"><i></i><i></i><i></i></div>
</header>

<section class="why">
  <h2 class="sec-title">WHY WE ARE DIFFERENCE</h2>
  <p class="sec-sub">Fresh ideas made for you</p>
  <div class="cards">
    <div class="card"><div class="photo" role="img" aria-label="Green juice in a glass with straw" style="background:linear-gradient(160deg,#8aa860,#5b7a3a)"></div><span>Fresh juice with high quality</span></div>
    <div class="card"><div class="photo" role="img" aria-label="Red berry smoothie in glasses" style="background:linear-gradient(160deg,#d88a9a,#9a2a44)"></div><span>Fresh juice with high quality</span></div>
    <div class="card"><div class="photo" role="img" aria-label="Purple juice with straw and fruit" style="background:linear-gradient(160deg,#dcd8c8,#7a3a6a)"></div><span>Fresh juice with high quality</span></div>
  </div>
  <div class="arrow"><svg width="10" height="16" viewBox="0 0 10 16"><path d="M2 2l6 6-6 6" stroke="#fff" stroke-width="2" fill="none"/></svg></div>
</section>

<section class="post">
  <div class="photo" role="img" aria-label="Happy friends raising glasses of juice around a dinner table"></div>
  <div class="post-body">
    <h2>YOUR FIRST POST WILL BE HERE</h2>
    <p>Fresh juice is one of the easiest ways to add more fruit and greens to your day. In this post we share how we started blending every morning, which produce works best for each season, and how small daily habits can lead to lasting health and weight goals. You will learn which blends give steady energy, which ones help you rest, and how to keep costs low by buying smart. Every recipe is tested in a home kitchen with common tools, so anyone can follow along. <b>Read more</b></p>
    <div class="signup">
      <label>Sign up for free weekly recipes</label>
      <div class="signup-row">
        <span class="signup-field">Your email address</span>
        <span class="signup-btn">SIGN UP</span>
      </div>
    </div>
  </div>
</section>

<section class="videos">
  <h2 class="sec-title">VIDEOS HERE</h2>
  <p class="sec-sub">Watch how each blend is made step by step</p>
  <div class="clips">
    <div class="clip" role="img" aria-label="Sliced oranges, lemons and bananas on a wooden board" style="width:328px;background:linear-gradient(135deg,#f0a030,#e6c060 50%,#6a4a2a)"></div>
    <div class="clip" role="img" aria-label="Pomegranate and red fruit slices on a plate" style="width:348px;background:linear-gradient(135deg,#f2e6d8,#c8303a 60%,#8a1a22)"></div>
  </div>
</section>

<div class="map" role="img" aria-label="Street map of the city location"></div>

<footer class="footer">
  <div class="brand">PRESSED TONIC</div>
  <small>ALL RIGHTS RESERVED © PRESSED TONIC</small>
  <div class="social"><i></i><i></i><i></i><i></i></div>
</footer>
</body>
</html>
```